Business cards and stationary for a health and wellbeing company
Lumen Forms
Business cards and stationary for a health and wellbeing company - Health
Creative Brief
Bright & Fun-filled
Jolene prescott
Director
PO Box
sales@lumenforms.com.au
www.lumenforms.com.au
Hi, I am happy to have a wide selection of fonts and designs. Lumen Forms is a health conscious Australian business that sells protein, supplements, health equipment, meditation and beauty products. We pride ourselves on great customer service, great products and a true passion for feeling and looking good. Our target market is females aged 18-60 years of age, mums and woman who want to feel amazing. Colour • Pink • White • Blue • Purple
Im open to different designs.
JolenePrescott JolenePrescott
Hi Everyone, Thank you so much for your great designs! I love the bright colours and lines that flow rather than straight and sharp. Could you please show me the front as well as the back of the business cards. I am wanting to change the font on my logo? I am wanting it so that the word Lumen sits above the word forms. Looking forward to some great designs! Thanks!

```html
<!DOCTYPE html>
<html lang="en">
<head>
<meta charset="utf-8">
<title>Lumen Forms – Business Cards</title>
<link href="https://fonts.googleapis.com/css2?family=Montserrat:wght@400;600;700&display=swap" rel="stylesheet">
<style>
  :root {
    --page-bg: #eef0f3;
    --card-white: #ffffff;
    --brand-pink: #d41db4;
    --brand-pink-deep: #b5129a;
    --brand-blue: #1db4e8;
    --brand-purple: #8e3fc9;
    --ink-light: #ffffff;
    --card-shadow: rgba(40, 30, 60, 0.18);
  }
  * { box-sizing: border-box; margin: 0; padding: 0; }
  html, body {
    width: 1200px; height: 901px; overflow: hidden;
    background: var(--page-bg);
    font-family: "Montserrat", sans-serif;
  }
  .stage {
    position: relative; width: 1200px; height: 901px;
    display: flex; align-items: center; justify-content: center; gap: 60px;
  }
  .card {
    position: relative; width: 510px; height: 300px;
    border-radius: 28px; overflow: hidden;
    background: var(--card-white);
    box-shadow: 0 14px 34px var(--card-shadow);
  }
  .card-waves { position: absolute; inset: 0; width: 100%; height: 100%; }
  .brand {
    position: absolute; display: flex; align-items: center; gap: 12px;
    font-weight: 700; color: var(--brand-purple);
  }
  .brand-dot {
    border-radius: 50%; background: var(--brand-purple);
  }
  .brand-name { line-height: 0.95; }
  .card-front .brand { left: 150px; top: 38px; font-size: 30px; }
  .card-front .brand-dot { width: 44px; height: 44px; }
  .card-back .brand {
    left: 50%; top: 50%; transform: translate(-50%, -50%);
    font-size: 40px;
  }
  .card-back .brand-dot { width: 60px; height: 60px; }
  .holder {
    position: absolute; left: 30px; top: 168px; color: var(--ink-light);
  }
  .holder-name { font-size: 17px; font-weight: 600; letter-spacing: 1px; text-transform: uppercase; }
  .holder-role { font-size: 11px; margin-top: 3px; opacity: 0.9; }
  .holder-address { font-size: 11px; margin-top: 16px; line-height: 1.5; }
  .contacts {
    position: absolute; right: 28px; top: 180px; color: var(--ink-light);
    list-style: none; font-size: 11px; text-align: right;
  }
  .contacts li {
    display: flex; align-items: center; justify-content: flex-end; gap: 8px;
    margin-bottom: 7px;
  }
  .contacts svg { width: 12px; height: 12px; fill: var(--ink-light); }
</style>
</head>
<body>
<main class="stage">

  <section class="card card-front" aria-label="Business card front">
    <svg class="card-waves" viewBox="0 0 510 300" preserveAspectRatio="none" aria-hidden="true">
      <path d="M0 150 C120 110 250 150 340 120 C420 95 470 110 510 100 L510 300 L0 300 Z" fill="var(--brand-pink)"/>
      <path d="M0 142 C120 100 250 140 340 110 C420 84 470 100 510 90" fill="none" stroke="var(--brand-blue)" stroke-width="7"/>
      <path d="M0 300 L0 250 C150 230 320 280 510 240 L510 300 Z" fill="var(--brand-pink-deep)" opacity="0.35"/>
    </svg>

    <div class="brand">
      <span class="brand-dot"></span>
      <span class="brand-name">Lumen<br>Forms</span>
    </div>

    <div class="holder">
      <p class="holder-name">Dana Whitfield</p>
      <p class="holder-role">Managing Director</p>
      <p class="holder-address">12 Ashgrove Lane<br>Harbour Road 4G2</p>
    </div>

    <ul class="contacts">
      <li>010 555 0142
        <svg viewBox="0 0 24 24"><path d="M6.6 10.8a15 15 0 0 0 6.6 6.6l2.2-2.2a1 1 0 0 1 1-.25 11 11 0 0 0 3.6.6 1 1 0 0 1 1 1V20a1 1 0 0 1-1 1A17 17 0 0 1 3 4a1 1 0 0 1 1-1h3.5a1 1 0 0 1 1 1 11 11 0 0 0 .6 3.6 1 1 0 0 1-.25 1z"/></svg>
      </li>
      <li>010 555 0143
        <svg viewBox="0 0 24 24"><rect x="6" y="2" width="12" height="20" rx="2"/></svg>
      </li>
      <li>sales@lumenforms.com.au
        <svg viewBox="0 0 24 24"><path d="M2 5h20v14H2z M2 5l10 8 10-8" /></svg>
      </li>
      <li>www.lumenforms.com.au
        <svg viewBox="0 0 24 24"><circle cx="12" cy="12" r="10"/></svg>
      </li>
    </ul>
  </section>

  <section class="card card-back" aria-label="Business card back">
    <div class="brand">
      <span class="brand-dot"></span>
      <span class="brand-name">Lumen<br>Forms</span>
    </div>
  </section>

</main>
</body>
</html>
```